Cedar Harbor Business Cards For New Startup

I am looking for you to design some business cards for a new startup https://cedarharborhub.com. I have supplied logo, brand guidelines and our signatures as a guide.

We need this to reflect the brand guidelines and the website for brand consistency,

What is Cedar Harbor?

Mallorca's Business Growth Community
Join your new business community full of passionate entrepreneurs who
love to solve problems and help each other grow together!

Any questions you can ask.

Target Market(s)

Business to Business

Contact Information for Business Card

These are attached (signatures) to the job

Font styles to use
Other font styles liked:
• Open Sans

Requirements
Must have
• Match design guidelines
Nice to have
• Photos of our faces so people remember us

```html
<!DOCTYPE html>
<html lang="en">
<head>
<meta charset="utf-8">
<title>Cedar Harbor Business Cards</title>
<link rel="stylesheet" href="https://fonts.googleapis.com/css2?family=Lato:wght@300;400;700&display=swap">
<style>
  :root {
    --backdrop: #3b322d;
    --card: #0d0d0d;
    --card-edge: #1a1a1a;
    --olive: #9c9a1e;
    --text: #e6e6e6;
    --silver: #c9c9c9;
    --band: #6f84a8;
    --photo-dark: #1c1f26;
    --photo-mid: #44506a;
  }
  * { margin: 0; padding: 0; box-sizing: border-box; }
  html, body { width: 1200px; height: 844px; overflow: hidden; }
  body {
    background: var(--backdrop);
    font-family: "Lato", sans-serif;
    position: relative;
  }
  .card {
    position: absolute;
    top: 272px;
    width: 520px;
    height: 300px;
    background: var(--card);
    border: 1px solid var(--card-edge);
    border-radius: 4px;
    overflow: hidden;
    box-shadow: 0 6px 18px rgba(0,0,0,.45);
  }
  .card-front { left: 50px; }
  .card-back { left: 630px; }

  /* front */
  .portrait {
    position: absolute;
    left: 0; bottom: 0;
    width: 240px; height: 220px;
    background: radial-gradient(ellipse at 55% 40%, var(--photo-mid) 0%, var(--photo-dark) 70%, var(--card) 100%);
  }
  .accent-band {
    position: absolute;
    left: 240px; right: 0; bottom: 0;
    height: 12px;
    background: var(--band);
  }
  .brand {
    position: absolute;
    display: flex;
    align-items: center;
    gap: 12px;
  }
  .brand-front { left: 258px; top: 52px; color: var(--olive); font-size: 24px; }
  .brand-mark {
    border-radius: 50%;
    border: 2px solid currentColor;
    flex: none;
  }
  .brand-front .brand-mark { width: 38px; height: 38px; }
  .brand-name { font-weight: 400; letter-spacing: .5px; }

  .details { position: absolute; left: 258px; top: 112px; color: var(--text); }
  .person-name { color: var(--olive); font-weight: 700; font-size: 20px; letter-spacing: .3px; }
  .person-role, .person-company { font-size: 14px; font-weight: 300; line-height: 1.35; }
  .contact-list { list-style: none; margin-top: 14px; font-size: 14px; font-weight: 300; }
  .contact-list li { display: flex; align-items: center; gap: 8px; line-height: 1.55; }
  .contact-list svg { width: 12px; height: 12px; fill: var(--olive); flex: none; }

  /* back */
  .brand-back {
    left: 50%; top: 92px;
    transform: translateX(-50%);
    color: var(--silver);
    font-size: 30px;
    gap: 16px;
  }
  .brand-back .brand-mark { width: 54px; height: 54px; }
  .social-row {
    position: absolute;
    left: 50%; top: 190px;
    transform: translateX(-50%);
    display: flex;
    align-items: center;
    gap: 10px;
  }
  .rule { width: 70px; height: 1px; background: var(--silver); opacity: .7; }
  .social-dot {
    width: 20px; height: 20px;
    border-radius: 50%;
    border: 1.5px solid var(--silver);
  }
</style>
</head>
<body>

<section class="card card-front">
  <div class="portrait" role="img" aria-label="Portrait photo of the founder"></div>
  <div class="accent-band"></div>

  <div class="brand brand-front">
    <span class="brand-mark"></span>
    <span class="brand-name">CEDAR HARBOR</span>
  </div>

  <div class="details">
    <p class="person-name">DANIEL MARSH</p>
    <p class="person-role">Founder &amp; Growth Hacker</p>
    <p class="person-company">Cedar Harbor</p>
    <ul class="contact-list">
      <li>
        <svg viewBox="0 0 24 24" aria-hidden="true"><path d="M6.6 10.8a15 15 0 0 0 6.6 6.6l2.2-2.2c.3-.3.7-.4 1-.2 1.1.4 2.3.6 3.6.6.6 0 1 .4 1 1V20c0 .6-.4 1-1 1A17 17 0 0 1 3 4c0-.6.4-1 1-1h3.5c.6 0 1 .4 1 1 0 1.3.2 2.5.6 3.6.1.3 0 .7-.2 1z"/></svg>
        +34 611 482 907
      </li>
      <li>
        <svg viewBox="0 0 24 24" aria-hidden="true"><path d="M2 5h20v14H2zm2 2v.5l8 5 8-5V7z"/></svg>
        dm@cedarharborhub.com
      </li>
      <li>
        <svg viewBox="0 0 24 24" aria-hidden="true"><circle cx="12" cy="12" r="10"/></svg>
        www.cedarharborhub.com
      </li>
    </ul>
  </div>
</section>

<section class="card card-back">
  <div class="brand brand-back">
    <span class="brand-mark"></span>
    <span class="brand-name">CEDAR HARBOR</span>
  </div>
  <div class="social-row" aria-label="Social profiles">
    <span class="rule"></span>
    <span class="social-dot"></span>
    <span class="social-dot"></span>
    <span class="social-dot"></span>
    <span class="social-dot"></span>
    <span class="social-dot"></span>
    <span class="rule"></span>
  </div>
</section>

</body>
</html>
```